Postcard Design

We are an exterior house wash company looking to design postcards to promote our business. we clean all types roofs and all types houses and all types of decks and all types of surfaces with a low pressure soft wash system.we also try to educate customers about the options and offer a maintenance program so their property is never dirty again, we use 100% biodegradable solutions to achieve results! our method outperforms traditional washing methods and remains clean 5 times longer,our method is 100% damage free,never pressure wash again!! our method is recommended by all manufactures,the NO pressure method,this method cleans so good you won't believe your eyes! guaranteed call today 207-418-3952 also want to add residential and commercial work and all hoa's(home owners assoc) also group rates available ,please use house washing logo provided,and roof washing logo,also the name of business is Tidecrest exterior house washing thanks

Industry/Entity Type

Biodegradable

Requirements
Must have
• company name (Tidecrest exterior house washing),logos provided(house wash,roof wash),also pics provided,thank you

```html
<!DOCTYPE html>
<html lang="en">
<head>
<meta charset="utf-8">
<title>Tidecrest exterior house washing – postcard</title>
<link href="https://fonts.googleapis.com/css2?family=Arimo:wght@400;700&display=swap" rel="stylesheet">
<style>
  :root{
    --page:#efefef;
    --card:#ffffff;
    --navy:#175a7c;
    --ink:#1c5677;
    --ocean:#2a9fd0;
    --sky:#6cc6ea;
    --pale:#9fdcf3;
    --white:#ffffff;
  }
  *{margin:0;padding:0;box-sizing:border-box}
  html,body{width:1200px;height:900px;overflow:hidden;background:var(--page);font-family:"Arimo",Arial,sans-serif}
  .postcard{position:absolute;background:var(--card)}
  .postcard svg{position:absolute;left:0;top:0}
  .postcard--front{left:40px;top:212px;width:520px;height:400px}
  .postcard--back{left:622px;top:210px;width:524px;height:404px}
  .text{position:absolute;line-height:1}
  .front-title{left:262px;top:170px;width:250px;text-align:center;color:var(--ink);font-size:27px;line-height:36px}
  .service-mark{position:absolute;display:flex;align-items:center;gap:4px;color:var(--ink);font-weight:700;font-size:11px;line-height:12px}
  .service-mark i{display:block;width:10px;height:10px;border-radius:50%;background:var(--ocean);flex:none}
  .service-mark--light{color:var(--white)}
  .service-mark--light i{background:var(--sky)}
  .pill{position:absolute;width:70px;height:26px;border-radius:50%;background:var(--navy);border:3px solid var(--white);box-shadow:0 0 0 2px var(--ocean);color:var(--white);font-weight:700;font-size:10px;display:flex;align-items:center;justify-content:center}
  .back-title{right:40px;top:22px;width:260px;text-align:center;color:var(--white);font-size:23px;line-height:32px}
  .benefits{left:10px;top:166px;width:300px;text-align:center;color:var(--ink);font-weight:700}
  .benefits p{line-height:21px}
  .benefits .sm{font-size:13px}
  .benefits .md{font-size:16px}
  .benefits .lg{font-size:19px}
  .call{right:14px;top:262px;color:var(--white);font-weight:700;font-size:26px}
  .phone{right:14px;top:292px;color:var(--white);font-weight:700;font-size:55px;letter-spacing:-1px}
  .footnote{left:52px;top:354px;color:var(--white);font-weight:700;font-size:11.5px;line-height:15px}
</style>
</head>
<body>

<section class="postcard postcard--front">
  <svg width="520" height="400" viewBox="0 0 520 400">
    <defs>
      <linearGradient id="house-before" x1="0" y1="0" x2="0" y2="1">
        <stop offset="0" stop-color="#6e8b5a"/>
        <stop offset="0.3" stop-color="#7a5f52"/>
        <stop offset="0.7" stop-color="#9a9488"/>
        <stop offset="1" stop-color="#3f6b2c"/>
      </linearGradient>
      <linearGradient id="house-after" x1="0" y1="0" x2="0" y2="1">
        <stop offset="0" stop-color="#8a6e5e"/>
        <stop offset="0.4" stop-color="#aaa69a"/>
        <stop offset="1" stop-color="#3e7a2b"/>
      </linearGradient>
      <clipPath id="front-clip"><rect x="7" y="7" width="506" height="386"/></clipPath>
    </defs>
    <g clip-path="url(#front-clip)">
      <path role="img" aria-label="Photo of the stone house before washing" d="M7 7 H500 Q430 120 7 192 Z" fill="url(#house-before)"/>
      <path role="img" aria-label="Photo of the stone house after washing" d="M7 225 Q330 255 515 393 H7 Z" fill="url(#house-after)"/>
      <path d="M7 198 Q380 140 515 8" fill="none" stroke="var(--ocean)" stroke-width="7"/>
      <path d="M7 190 Q400 110 515 2" fill="none" stroke="var(--navy)" stroke-width="3"/>
      <path d="M7 220 Q340 240 515 386" fill="none" stroke="var(--ocean)" stroke-width="7"/>
      <path d="M150 235 Q400 250 515 330" fill="none" stroke="var(--pale)" stroke-width="4"/>
      <ellipse cx="420" cy="198" rx="178" ry="96" fill="none" stroke="var(--navy)" stroke-width="4"/>
      <ellipse cx="425" cy="198" rx="170" ry="88" fill="var(--sky)"/>
    </g>
  </svg>
  <div class="pill" style="left:20px;top:16px">BEFORE</div>
  <div class="pill" style="left:410px;top:356px">AFTER</div>
  <div class="service-mark" style="left:82px;top:200px;width:72px"><i></i>Tidecrest Roof Care</div>
  <div class="service-mark" style="left:160px;top:200px;width:90px"><i></i>Tidecrest House Wash</div>
  <h1 class="text front-title">Tidecrest exterior house washing</h1>
</section>

<section class="postcard postcard--back">
  <svg width="524" height="404" viewBox="0 0 524 404">
    <defs><clipPath id="back-clip"><rect x="7" y="7" width="510" height="390"/></clipPath></defs>
    <g clip-path="url(#back-clip)">
      <rect x="7" y="7" width="510" height="390" fill="var(--navy)"/>
      <path d="M7 92 Q300 170 517 195 V232 Q300 250 7 385 Z" fill="var(--white)"/>
      <path d="M7 10 Q60 70 517 196" fill="none" stroke="var(--sky)" stroke-width="5"/>
      <path d="M7 30 Q70 80 517 198" fill="none" stroke="var(--ocean)" stroke-width="3"/>
      <path d="M7 395 Q150 265 517 228" fill="none" stroke="var(--ocean)" stroke-width="6"/>
      <ellipse cx="140" cy="196" rx="188" ry="92" fill="var(--ocean)"/>
      <ellipse cx="130" cy="196" rx="176" ry="86" fill="var(--navy)"/>
      <ellipse cx="126" cy="196" rx="170" ry="82" fill="var(--sky)"/>
    </g>
  </svg>
  <h2 class="text back-title">Tidecrest exterior house washing</h2>
  <div class="service-mark service-mark--light" style="left:268px;top:108px;width:96px"><i></i>Tidecrest Roof Care</div>
  <div class="service-mark service-mark--light" style="left:390px;top:108px;width:104px"><i></i>Tidecrest House Wash</div>
  <div class="text benefits">
    <p class="md">100% biodegradable <span class="sm">solutions</span></p>
    <p class="sm">traditional washing methods</p>
    <p class="md"><span class="sm">Remains clean</span> 5 times longer</p>
    <p class="lg">100% damage free</p>
  </div>
  <div class="text call">Call today</div>
  <div class="text phone">207-418-3952</div>
  <p class="text footnote">Our method is recommended by all manufactures,the NO pressure method,<br>this method cleans so good you won't believe your eyes!</p>
</section>

</body>
</html>
```